Professional Hairdresser needs powerful, clever, simple, modern business card

I need a professional, clever, powerful, bold, attractive, modern/simplistic business card.
I specialize in dimensional hair color, precision haircutting, modern classic design, and signature finishes.
I believe in advanced education, continued training with emphasis on perfect practice, and strive to be the best at what I do.
I am trained by the industry's best and have passion for what I do, I want my business card to reflect my talents, education, capabilities, signature color techniques and design and confidence.
I want to be known as reputable, bold, artistic, aware, classic yet modern, innovative, creative, dimensional, knowledgeable, and educated.
I want something bold, simple, elegant, modern, clever, and legible.
My personal style is progressive, modern, eclectic, clean with modern luxury comfort style.
I love the use of black and white, to creative visual interest and texture. I think putting black as a solid background with white bold font makes the words jump/glow to the eye. I also think a stark white background with bold black fonts looks great, maybe with a punch of red. It is simple, clean, elegant.
I have a QR code I would like to include on the card but have no idea how to make it visually pleasing or make sense.
I do not have a set logo and am not sure if this needs to be done first or if the business card should be done first.
Updates

Reason: Very difficult decision. All designers are amazing.

Reason: Difficult decisions

Reason: Need more time as yesterday was not able to work as much as possible with designers. They are all great and look forward to having time later to look at them.

Reason: Unexpected time delay.

Target Market(s)

Early 20's-mid 60's, female and male, fashion aware, people who can afford my prices, appreciate value

Industry/Entity Type

Training

Requirements
Must have
• I would like to incorporate the QR code I have if possible.
I would like to have my name and contact info.
I would like my logo (or maybe have my logo be RT in a font like listed below).
I would like the fonts to be modern, bold, clean, readable.
Fonts I have looked at are: The font used on the book called: Morvani An Age of Bright Shapes" I really love. I have looked at glyphwell.net for font and found "Georgiquas", but the designer wanted 200 euros which I just dont have at the time. Others I looked at include "Lin Libertine", Alien-Encounters-solid-regular-italic".
I love font used in the picture I included with the Tobias.Lindqvist ad.
Clean, modern, professional, legible, structured.
Nice to have
• I envision a black background with bold, modern, simple, font in white creating the effect of the words jumping off the card, visually apparent and glowing. Like a really expensive restaurant with a sign that you cant miss because the name is in bright white on black background, simple, bold, modern but not futuristic, powerful, clever, elegant, and draws the eye making it unforgetable. Perhaps layering black and white in order to where the font will be in white.
I see balance and chic.
Perhaps
Should not have
• I appreciate the trends in business design, but realize trends come and go and not sure if having something "trendy" is advisable for me. Having said that, I like creative modern design and sometimes current trends are important in design. I do like red as accent color, the primary blue color, blue on the PixelQuorum page, the masculine/florescent purple, and the neo bold yellow and the primary color shade of yellow.
I do not want clutter.
I do not want any fonts that are swirly, old-world calligraphy, script, or penmanship style.
I do not want picture of scissors, heads of old-school beauty school hair, or barber poles.

```html
<!DOCTYPE html>
<html lang="en">
<head>
<meta charset="utf-8">
<title>Rowan Tate — Hair Stylist</title>
<link rel="stylesheet" href="https://fonts.googleapis.com/css2?family=Inter:wght@300;400;700;800&display=swap">
<style>
  :root {
    --card-black: #000000;
    --ink-white: #ffffff;
    --accent-cyan: #00ffff;
  }
  html, body {
    margin: 0;
    padding: 0;
    width: 1200px;
    height: 686px;
    overflow: hidden;
    background: var(--card-black);
  }
  .card {
    position: relative;
    width: 1200px;
    height: 686px;
    background: var(--card-black);
    color: var(--ink-white);
    font-family: "Inter", "Helvetica Neue", Arial, sans-serif;
    overflow: hidden;
  }
  .wordmark {
    position: absolute;
    top: 88px;
    left: 50%;
    transform: translateX(-50%);
    margin: 0;
    text-align: left;
    white-space: nowrap;
    font-weight: 400;
  }
  .wordmark__first {
    display: block;
    line-height: 1;
    font-size: 52px;
    letter-spacing: -0.01em;
  }
  .wordmark__initial {
    font-size: 110px;
    font-weight: 800;
    letter-spacing: -0.03em;
  }
  .wordmark__last {
    display: block;
    line-height: 1;
    margin-top: -36px;
    font-size: 176px;
    font-weight: 700;
    letter-spacing: -0.045em;
  }
  .role {
    position: absolute;
    top: 361px;
    left: 0;
    right: 0;
    margin: 0;
    text-align: center;
    line-height: 1;
    font-size: 47px;
    font-weight: 300;
    letter-spacing: 0.01em;
  }
  .contact {
    position: absolute;
    top: 450px;
    left: 0;
    right: 0;
    margin: 0;
    text-align: center;
    line-height: 1;
    font-size: 44px;
    font-weight: 300;
    white-space: nowrap;
  }
  .contact__divider {
    display: inline-block;
    width: 14px;
    height: 14px;
    margin: 0 30px;
    border-radius: 50%;
    background: var(--ink-white);
    vertical-align: 0.18em;
  }
  .strand-border {
    position: absolute;
    left: 0;
    bottom: 0;
    width: 1200px;
    height: 137px;
    background: linear-gradient(to bottom, rgba(0, 255, 255, 0.35) 0%, var(--accent-cyan) 45%, var(--accent-cyan) 100%);
  }
</style>
</head>
<body>
  <main class="card">
    <h1 class="wordmark">
      <span class="wordmark__first"><span class="wordmark__initial">R</span>OWAN</span>
      <span class="wordmark__last">Tate</span>
    </h1>
    <p class="role">HAIR STYLIST</p>
    <p class="contact">
      <span class="contact__phone">310.555.0142</span><span class="contact__divider" aria-hidden="true"></span><span class="contact__email">HELLO@ROWANTATE.COM</span>
    </p>
    <div class="strand-border" role="img" aria-label="Cyan border of flame-like hair strands rising along the bottom edge"></div>
  </main>
</body>
</html>
```